Red Sea Boat trips in need of Business Card for Private Boat Tours

We need a Business card for a new business set-up in Egypt on the Red Sea for private snorkelling and boat excursions to one of the world's most beautiful reefs. We have wording logo already set-up which matches the boat but we need business cards to be bright and colourful with pictures of boat

Industry/Entity Type

Tourism

Contact Information for Business Card

Two Silver Herons (font provided) Boat Trips

```html
<!DOCTYPE html>
<html lang="en">
<head>
<meta charset="utf-8">
<title>Two Silver Herons – Business Card</title>
<link rel="stylesheet" href="https://fonts.googleapis.com/css2?family=Open+Sans:wght@400;600&family=Dancing+Script:wght@600&display=swap">
<style>
  :root {
    --page-bg: #e8e8e6;
    --card-bg: #2b2b2c;
    --card-edge: #1c1c1d;
    --ink-light: #f2f2f2;
    --ink-muted: #d4d4d4;
    --accent-teal: #2a9aa3;
    --emboss-grey: #5a5a5c;
    --sea-deep: #123f5a;
    --sea-mid: #1f7f94;
    --sea-shallow: #6fd3d8;
  }
  * { box-sizing: border-box; margin: 0; padding: 0; }
  html, body { width: 1200px; height: 804px; overflow: hidden; }
  body {
    background: var(--page-bg);
    font-family: "Open Sans", sans-serif;
    display: flex;
    align-items: center;
    justify-content: center;
    gap: 40px;
  }
  .card {
    position: relative;
    width: 540px;
    height: 310px;
    background: var(--card-bg);
    border-radius: 3px;
    box-shadow: 0 2px 0 var(--card-edge), 0 10px 24px rgba(0,0,0,0.18);
    overflow: hidden;
  }
  .card-front__photo {
    position: absolute;
    inset: 0;
    width: 100%;
    height: 100%;
  }
  .card-front__content {
    position: absolute;
    left: 28px;
    bottom: 22px;
    color: var(--ink-light);
  }
  .brand-name {
    font-weight: 600;
    font-size: 30px;
    line-height: 1.1;
    color: var(--ink-light);
    margin-bottom: 8px;
  }
  .person-name {
    font-family: "Dancing Script", cursive;
    font-weight: 600;
    font-size: 30px;
    line-height: 1;
    color: var(--accent-teal);
  }
  .person-role {
    font-size: 14px;
    color: var(--ink-muted);
    margin-bottom: 14px;
  }
  .address {
    font-size: 14px;
    line-height: 1.35;
    color: var(--ink-muted);
    margin-bottom: 12px;
  }
  .contact-list { list-style: none; }
  .contact-list li {
    display: flex;
    align-items: center;
    gap: 8px;
    font-size: 14px;
    line-height: 1.45;
    color: var(--ink-muted);
  }
  .contact-icon { width: 12px; height: 12px; flex: none; }
  .card-back {
    display: flex;
    align-items: center;
    justify-content: center;
  }
  .card-back .brand-name {
    font-size: 40px;
    color: var(--emboss-grey);
    margin: 0;
  }
</style>
</head>
<body>
  <section class="card card-front">
    <svg class="card-front__photo" viewBox="0 0 540 310" role="img" aria-label="Underwater photograph of a freediver swimming above a turquoise coral reef">
      <defs>
        <linearGradient id="sea" x1="0" y1="0" x2="1" y2="1">
          <stop offset="0" stop-color="var(--sea-deep)"/>
          <stop offset="0.55" stop-color="var(--sea-mid)"/>
          <stop offset="1" stop-color="var(--sea-shallow)"/>
        </linearGradient>
      </defs>
      <polygon points="190,0 540,0 540,215 470,230 410,190 330,175 270,150 215,120 175,95" fill="url(#sea)"/>
    </svg>
    <div class="card-front__content">
      <p class="brand-name">Two Silver Herons</p>
      <p class="person-name">Marcus Hale</p>
      <p class="person-role">Managing Director</p>
      <p class="address">Your Address, City<br>State, Zip 0000</p>
      <ul class="contact-list">
        <li>
          <svg class="contact-icon" viewBox="0 0 12 12"><path d="M3 1l2 2-1 1.5c.6 1.4 1.6 2.4 3 3L8.5 6.5l2 2-1 2C5 10.5 1.5 7 1.5 2.5z" fill="var(--accent-teal)"/></svg>
          044-987 654 321
        </li>
        <li>
          <svg class="contact-icon" viewBox="0 0 12 12"><rect x="1" y="2.5" width="10" height="7" rx="1" fill="var(--accent-teal)"/><path d="M1.5 3l4.5 3.5L10.5 3" stroke="var(--card-bg)" fill="none" stroke-width="1"/></svg>
          hello@silverherons.com
        </li>
        <li>
          <svg class="contact-icon" viewBox="0 0 12 12"><circle cx="6" cy="6" r="5" fill="var(--accent-teal)"/><path d="M1 6h10M6 1c2 2.5 2 7.5 0 10M6 1c-2 2.5-2 7.5 0 10" stroke="var(--card-bg)" stroke-width="0.8" fill="none"/></svg>
          www.silverherons.com
        </li>
      </ul>
    </div>
  </section>

  <section class="card card-back">
    <p class="brand-name">Two Silver Herons</p>
  </section>
</body>
</html>
```